Tradeshow Display

I need to create 3 panels each measuring 37.75 inches wide by 89.25 inches tall. I would like to have it be a uniform look and even have parts of it be a continuation on all 3 panels.

Our website is www.veltragrid.com and would like for the 3 panels to represent our services with a big emphasis on technology driven solutions and Ai

```html
<!DOCTYPE html>
<html lang="en">
<head>
<meta charset="utf-8">
<title>Veltragrid Tradeshow Panels</title>
<link href="https://fonts.googleapis.com/css2?family=Poppins:wght@400;500;600;700;800&family=Russo+One&display=swap" rel="stylesheet">
<style>
  :root {
    --stage: #5f6368;
    --paper: #ffffff;
    --lime: #9ccb3b;
    --sky: #1c9ae2;
    --navy: #1570b8;
    --ink: #1f2a33;
    --muted: #7c7f88;
    --photo-deep: #1b2735;
    --photo-mid: #3c5670;
    --photo-light: #7f9ab3;
    --pill-line: #3b4a5a;
  }
  * { box-sizing: border-box; margin: 0; padding: 0; }
  html, body { width: 800px; height: 1200px; overflow: hidden; }
  body {
    background: var(--stage);
    font-family: "Poppins", sans-serif;
    position: relative;
  }
  .display { position: absolute; left: 16px; top: 316px; display: flex; gap: 24px; }
  .panel {
    position: relative; width: 240px; height: 568px;
    background: var(--paper); overflow: hidden;
  }
  .panel-art { position: absolute; inset: 0; width: 240px; height: 568px; }
  .brand {
    position: absolute; display: flex; align-items: center; gap: 6px;
    font-weight: 700; color: var(--navy); letter-spacing: 0.5px;
  }
  .brand-dot { width: 12px; height: 12px; border-radius: 50%; background: var(--lime); }
  .contact { position: absolute; left: 0; right: 0; text-align: center; }
  .contact-phone {
    font-family: "Russo One", sans-serif; font-size: 21px; color: var(--ink);
    display: flex; justify-content: center; align-items: center; gap: 5px; letter-spacing: 0.5px;
  }
  .contact-web {
    font-family: "Russo One", sans-serif; font-size: 17px; letter-spacing: 1px; margin-top: 2px;
  }
  .contact-web.on-green { color: var(--paper); }
  .contact-web.on-white { color: var(--navy); }

  /* Panel 1 */
  .hero-copy { position: absolute; top: 302px; left: 0; right: 0; text-align: center; }
  .hero-kicker { font-weight: 800; font-size: 20px; color: var(--lime); line-height: 1; }
  .hero-title { font-weight: 800; font-size: 37px; color: var(--navy); line-height: 1; margin-top: 2px; letter-spacing: -0.5px; }
  .hero-tag {
    display: inline-block; background: var(--ink); color: var(--paper);
    font-weight: 700; font-size: 16px; padding: 1px 8px; border-radius: 3px; margin-top: 3px; letter-spacing: 0.5px;
  }
  .hero-lines { margin-top: 12px; font-size: 12.5px; font-weight: 500; color: var(--muted); line-height: 1.3; }

  /* Panel 2 */
  .services-badge {
    position: absolute; top: 124px; left: 47px; width: 146px; height: 22px;
    background: var(--lime); color: var(--paper); font-weight: 700; font-size: 13px;
    text-align: center; line-height: 22px; border-radius: 2px; letter-spacing: 0.8px;
  }
  .service { position: absolute; width: 110px; text-align: center; }
  .service-label { font-weight: 600; font-size: 12.5px; color: var(--muted); line-height: 1.25; margin-top: 6px; }

  /* Panel 3 */
  .provide-title { position: absolute; top: 190px; left: 25px; font-weight: 800; font-size: 14px; color: var(--navy); letter-spacing: 0.5px; }
  .provide-list { position: absolute; top: 216px; left: 23px; width: 198px; list-style: none; }
  .provide-item {
    height: 16px; border: 1px solid var(--pill-line); border-radius: 8px; margin-bottom: 8.6px;
    display: flex; align-items: center; gap: 5px; padding-left: 4px;
    font-size: 8.6px; font-weight: 500; color: var(--ink);
  }
  .provide-tick { width: 9px; height: 9px; flex: none; }
</style>
</head>
<body>
<main class="display">

  <!-- Panel 1: headline -->
  <section class="panel panel-hero">
    <svg class="panel-art" viewBox="0 0 240 568">
      <defs>
        <linearGradient id="heroPhoto" x1="0" y1="0" x2="1" y2="1">
          <stop offset="0" stop-color="#2d4460"/><stop offset="0.55" stop-color="#3d5a7a"/><stop offset="1" stop-color="#1d2836"/>
        </linearGradient>
      </defs>
      <path role="img" aria-label="Photo of a business hand touching a network of technology icons"
            fill="url(#heroPhoto)"
            d="M0,160 C50,152 92,72 152,54 C205,40 238,80 238,150 C238,225 220,268 180,278 C130,290 60,262 0,270 Z"/>
      <path d="M0,150 C50,143 90,62 150,44 C195,31 228,48 240,72" fill="none" stroke="var(--sky)" stroke-width="6"/>
      <path d="M0,160 C50,152 92,72 152,54 C198,42 228,62 238,95" fill="none" stroke="var(--lime)" stroke-width="6"/>
      <path d="M0,268 C50,258 110,288 160,282 C205,277 225,258 232,238" fill="none" stroke="var(--lime)" stroke-width="6"/>
      <path d="M0,280 C60,268 110,298 165,292 C208,287 230,268 236,248" fill="none" stroke="var(--sky)" stroke-width="6"/>
      <path d="M0,498 C70,478 140,475 200,488 C222,494 232,502 236,510 L236,568 L0,568 Z" fill="var(--sky)"/>
      <path d="M0,508 C70,490 140,488 195,502 C222,511 230,530 232,568 L0,568 Z" fill="var(--lime)"/>
    </svg>
    <div class="brand" style="top:38px;left:16px;font-size:19px;"><span class="brand-dot"></span>VELTRAGRID</div>
    <div class="hero-copy">
      <div class="hero-kicker">THE FUTURE</div>
      <div class="hero-title">OF RCM</div>
      <div class="hero-tag">STARTS HERE</div>
      <p class="hero-lines">Tech-driven RCM,<br>your path to gain ,<br>Trust and profits, we sustain!</p>
    </div>
    <div class="contact" style="top:516px;">
      <div class="contact-phone">
        <svg width="16" height="16" viewBox="0 0 16 16"><circle cx="8" cy="8" r="8" fill="var(--navy)"/><path d="M5.2,4 L6.8,4 L7.4,6 L6.5,6.8 C7,8 8,9 9.2,9.5 L10,8.6 L12,9.2 L12,10.8 C8,11 5,8 5.2,4 Z" fill="#fff"/></svg>
        877-555-0192
      </div>
      <div class="contact-web on-green">www.veltragrid.com</div>
    </div>
  </section>

  <!-- Panel 2: services -->
  <section class="panel panel-services">
    <svg class="panel-art" viewBox="0 0 240 568">
      <defs>
        <linearGradient id="agentPhoto" x1="0" y1="0" x2="1" y2="1">
          <stop offset="0" stop-color="#2a3e55"/><stop offset="0.6" stop-color="#1c2a3b"/><stop offset="1" stop-color="#3a3a40"/>
        </linearGradient>
        <linearGradient id="svcPhoto" x1="0" y1="0" x2="1" y2="1">
          <stop offset="0" stop-color="#9fb4c8"/><stop offset="1" stop-color="#2f4a66"/>
        </linearGradient>
      </defs>
      <path role="img" aria-label="Photo of a support agent with headset working at a computer"
            fill="url(#agentPhoto)"
            d="M14,0 H240 V84 C185,108 130,122 75,120 C40,118 18,95 14,60 Z"/>
      <path d="M4,0 C0,50 20,105 75,124" fill="none" stroke="var(--sky)" stroke-width="5"/>
      <path d="M12,0 C8,55 30,112 80,122 C140,128 190,108 240,84" fill="none" stroke="var(--lime)" stroke-width="5"/>
      <g fill="url(#svcPhoto)" stroke="var(--lime)" stroke-width="1.2" stroke-dasharray="3 2">
        <circle role="img" aria-label="Photo of revenue charts on a tablet" cx="68" cy="203" r="32"/>
        <circle role="img" aria-label="Photo of auditors reviewing reports" cx="170" cy="207" r="32"/>
        <circle role="img" aria-label="Photo of a hand filling an insurance form" cx="68" cy="343" r="32"/>
        <circle role="img" aria-label="Photo of a consulting team at a desk" cx="170" cy="343" r="32"/>
      </g>
      <g stroke="var(--lime)" stroke-width="1" stroke-dasharray="3 2">
        <line x1="120" y1="174" x2="120" y2="285"/>
        <line x1="120" y1="315" x2="120" y2="410"/>
        <line x1="18" y1="300" x2="110" y2="300"/>
        <line x1="130" y1="300" x2="222" y2="300"/>
      </g>
    </svg>
    <div class="services-badge">OUR SERVICES</div>
    <div class="service" style="left:13px;top:237px;"><div class="service-label">Revenue<br>Cycle<br>Management</div></div>
    <div class="service" style="left:115px;top:241px;"><div class="service-label">Auditing<br>Services</div></div>
    <div class="service" style="left:13px;top:377px;"><div class="service-label">Insurance<br>Pre-Check</div></div>
    <div class="service" style="left:115px;top:377px;"><div class="service-label">Practice<br>Consulting</div></div>
    <div class="brand" style="top:470px;left:0;right:0;justify-content:center;font-size:17px;"><span class="brand-dot"></span>VELTRAGRID</div>
    <div class="contact" style="top:512px;">
      <div class="contact-phone">
        <svg width="16" height="16" viewBox="0 0 16 16"><circle cx="8" cy="8" r="8" fill="var(--navy)"/><path d="M5.2,4 L6.8,4 L7.4,6 L6.5,6.8 C7,8 8,9 9.2,9.5 L10,8.6 L12,9.2 L12,10.8 C8,11 5,8 5.2,4 Z" fill="#fff"/></svg>
        877-555-0192
      </div>
      <div class="contact-web on-white">www.veltragrid.com</div>
    </div>
  </section>

  <!-- Panel 3: AI and service list -->
  <section class="panel panel-provide">
    <svg class="panel-art" viewBox="0 0 240 568">
      <defs>
        <linearGradient id="bandPhoto" x1="0" y1="0" x2="1" y2="0">
          <stop offset="0" stop-color="#2a3644"/><stop offset="1" stop-color="#1a2430"/>
        </linearGradient>
        <radialGradient id="aiPhoto" cx="0.45" cy="0.4" r="0.7">
          <stop offset="0" stop-color="#a9bfd2"/><stop offset="0.6" stop-color="#4a6580"/><stop offset="1" stop-color="#1e2c3b"/>
        </radialGradient>
      </defs>
      <path role="img" aria-label="Photo of an office workspace at night"
            fill="url(#bandPhoto)" d="M0,0 H240 V20 C170,22 90,50 0,85 Z"/>
      <path d="M0,85 C90,50 170,22 240,20" fill="none" stroke="var(--paper)" stroke-width="3"/>
      <circle cx="175" cy="110" r="74" fill="var(--lime)"/>
      <circle role="img" aria-label="Photo of hands typing on a keyboard beneath a glowing AI brain interface"
              cx="180" cy="110" r="64" fill="url(#aiPhoto)"/>
      <path d="M0,500 C70,476 140,470 200,480 C222,484 235,490 240,495 L240,568 L0,568 Z" fill="var(--sky)"/>
      <path d="M14,568 C14,530 40,505 90,500 C150,494 200,500 240,510 L240,568 Z" fill="var(--lime)"/>
    </svg>
    <div class="brand" style="top:152px;left:24px;font-size:15px;"><span class="brand-dot"></span>VELTRAGRID</div>
    <h2 class="provide-title">WE PROVIDE</h2>
    <ul class="provide-list">
      <li class="provide-item"><svg class="provide-tick" viewBox="0 0 10 10"><circle cx="5" cy="5" r="5" fill="var(--sky)"/><path d="M2.8,5.2 L4.4,6.7 L7.3,3.6" fill="none" stroke="#fff" stroke-width="1.3"/></svg>Benefit Verification</li>
      <li class="provide-item"><svg class="provide-tick" viewBox="0 0 10 10"><circle cx="5" cy="5" r="5" fill="var(--sky)"/><path d="M2.8,5.2 L4.4,6.7 L7.3,3.6" fill="none" stroke="#fff" stroke-width="1.3"/></svg>Prior Authorization</li>
      <li class="provide-item"><svg class="provide-tick" viewBox="0 0 10 10"><circle cx="5" cy="5" r="5" fill="var(--sky)"/><path d="M2.8,5.2 L4.4,6.7 L7.3,3.6" fill="none" stroke="#fff" stroke-width="1.3"/></svg>Payment Posting and Denials</li>
      <li class="provide-item"><svg class="provide-tick" viewBox="0 0 10 10"><circle cx="5" cy="5" r="5" fill="var(--sky)"/><path d="M2.8,5.2 L4.4,6.7 L7.3,3.6" fill="none" stroke="#fff" stroke-width="1.3"/></svg>Solution-Based Appeals</li>
      <li class="provide-item"><svg class="provide-tick" viewBox="0 0 10 10"><circle cx="5" cy="5" r="5" fill="var(--sky)"/><path d="M2.8,5.2 L4.4,6.7 L7.3,3.6" fill="none" stroke="#fff" stroke-width="1.3"/></svg>Charge Entry / Scrubbing</li>
      <li class="provide-item"><svg class="provide-tick" viewBox="0 0 10 10"><circle cx="5" cy="5" r="5" fill="var(--sky)"/><path d="M2.8,5.2 L4.4,6.7 L7.3,3.6" fill="none" stroke="#fff" stroke-width="1.3"/></svg>Accounts Receivables Management</li>
      <li class="provide-item"><svg class="provide-tick" viewBox="0 0 10 10"><circle cx="5" cy="5" r="5" fill="var(--sky)"/><path d="M2.8,5.2 L4.4,6.7 L7.3,3.6" fill="none" stroke="#fff" stroke-width="1.3"/></svg>Reports</li>
      <li class="provide-item"><svg class="provide-tick" viewBox="0 0 10 10"><circle cx="5" cy="5" r="5" fill="var(--sky)"/><path d="M2.8,5.2 L4.4,6.7 L7.3,3.6" fill="none" stroke="#fff" stroke-width="1.3"/></svg>Drug Audit</li>
      <li class="provide-item"><svg class="provide-tick" viewBox="0 0 10 10"><circle cx="5" cy="5" r="5" fill="var(--sky)"/><path d="M2.8,5.2 L4.4,6.7 L7.3,3.6" fill="none" stroke="#fff" stroke-width="1.3"/></svg>Cost-Benefit Analysis</li>
      <li class="provide-item"><svg class="provide-tick" viewBox="0 0 10 10"><circle cx="5" cy="5" r="5" fill="var(--sky)"/><path d="M2.8,5.2 L4.4,6.7 L7.3,3.6" fill="none" stroke="#fff" stroke-width="1.3"/></svg>Coding Support</li>
    </ul>
    <div class="contact" style="top:516px;padding-left:12px;">
      <div class="contact-phone">
        <svg width="16" height="16" viewBox="0 0 16 16"><circle cx="8" cy="8" r="8" fill="var(--navy)"/><path d="M5.2,4 L6.8,4 L7.4,6 L6.5,6.8 C7,8 8,9 9.2,9.5 L10,8.6 L12,9.2 L12,10.8 C8,11 5,8 5.2,4 Z" fill="#fff"/></svg>
        877-555-0192
      </div>
      <div class="contact-web on-green">www.veltragrid.com</div>
    </div>
  </section>

</main>
</body>
</html>
```